Business Card Design Project

Looking to have a new business card created.

The card needs to be sort of two cards attached in the centre creating a flip card so we can write in the centre.

First side with my information at the director / licensee and then the back side with my assistant's details.

Inside with minimal information, facebook link/sign and then lines to write on.

www.norlandestates.com.au is my website to show colours and designs that I like.

Target Market(s)

Property Owners, Property Investors, Tenants, rental clients, Tradesman.

Industry/Entity Type

Business

Requirements
Must have
• Professional & symmetrical.

Am getting pro photos for myself & assistance, so a space for these once received.

```html
<!DOCTYPE html>
<html lang="en">
<head>
<meta charset="utf-8">
<title>Norland Estates – Flip Business Card</title>
<link href="https://fonts.googleapis.com/css2?family=Poiret+One&family=Open+Sans:wght@300;400;700&display=swap" rel="stylesheet">
<style>
  :root {
    --page: #eef0f1;
    --paper: #ffffff;
    --ink: #1c1c1c;
    --ink-soft: #444444;
    --brand: #5f7c8e;
    --frame: #3f6173;
    --night-1: #0a1a22;
    --night-2: #183d4c;
    --night-3: #0e2630;
    --pencil: #2b4a8a;
    --pencil-dark: #1a2f5c;
    --white: #ffffff;
  }
  * { box-sizing: border-box; margin: 0; padding: 0; }
  html, body { width: 1095px; height: 1200px; overflow: hidden; }
  body {
    background: var(--page);
    font-family: "Open Sans", Arial, sans-serif;
    color: var(--ink);
    position: relative;
  }
  .card { position: absolute; box-shadow: 0 2px 8px rgba(0,0,0,.18); overflow: hidden; }
  .brand-name {
    font-family: "Poiret One", "Open Sans", sans-serif;
    font-weight: 400;
    color: var(--brand);
    white-space: nowrap;
  }

  /* Inside spread */
  .inside { left: 175px; top: 356px; width: 771px; height: 219px; background: var(--paper); }
  .inside .info { position: absolute; left: 20px; top: 18px; }
  .info-row { position: relative; padding-left: 20px; margin-bottom: 12px; font-size: 12px; line-height: 16px; color: var(--ink-soft); }
  .info-row::before { content: ""; position: absolute; left: 0; top: 50%; width: 10px; height: 10px; margin-top: -4px; background: var(--ink); border-radius: 2px; }
  .info-row .text { border-left: 2px solid var(--ink); padding-left: 6px; display: block; }
  .info-row strong { color: var(--ink); font-weight: 700; }
  .inside .brand-name { position: absolute; left: 262px; top: 22px; font-size: 17px; line-height: 1; }
  .inside .brand-name::after { content: ""; display: inline-block; width: 7px; height: 7px; margin-left: 4px; background: var(--brand); border-radius: 50%; vertical-align: middle; }
  .pencil { position: absolute; left: 402px; top: 12px; }
  .write-lines { position: absolute; left: 413px; top: 20px; width: 320px; }
  .write-line { height: 17.5px; border-bottom: 1px dotted #777; }
  .inside .rule { position: absolute; left: 0; right: 0; top: 170px; border-top: 1.5px solid var(--ink-soft); }
  .inside .web { position: absolute; left: 0; right: 0; top: 178px; text-align: center; font-family: "Poiret One", sans-serif; font-size: 23px; letter-spacing: 11px; color: var(--ink); }

  /* Director card */
  .director { left: 161px; top: 592px; width: 387px; height: 247px; background: var(--paper); border: 5px solid var(--frame); border-left-width: 8px; }
  .director .brand-name { position: absolute; left: 22px; top: 22px; font-size: 44px; line-height: 1; }
  .director .tagline { position: absolute; left: 26px; top: 72px; font-size: 12px; color: var(--brand); font-weight: 300; }
  .director .person { position: absolute; right: 22px; top: 76px; text-align: right; color: var(--brand); font-size: 10.5px; line-height: 15px; font-weight: 300; }
  .director .person .name { font-size: 12.5px; letter-spacing: 1px; }
  .director .contacts { position: absolute; left: 22px; top: 143px; color: var(--brand); font-size: 10.5px; line-height: 17px; font-weight: 300; }
  .contacts div, .night .phone { display: flex; align-items: center; gap: 4px; }
  .director .skyline { position: absolute; right: 0; bottom: 0; width: 137px; height: 72px; background: linear-gradient(to top, #e3eaee, #f4f7f8 70%, rgba(255,255,255,0)); }

  /* Assistant card */
  .night { left: 563px; top: 617px; width: 389px; height: 223px; background: radial-gradient(ellipse at 55% 40%, var(--night-2), var(--night-3) 55%, var(--night-1)); color: var(--white); }
  .night .badge { position: absolute; left: 20px; top: 25px; width: 155px; height: 64px; background: var(--white); border-radius: 32px; display: flex; flex-direction: column; align-items: center; justify-content: center; }
  .night .badge .brand-name { font-size: 24px; line-height: 1; }
  .night .badge .tagline { font-size: 8px; color: var(--brand); margin-top: 3px; }
  .night .person { position: absolute; right: 23px; top: 66px; text-align: right; }
  .night .person .name { font-size: 14px; font-weight: 700; }
  .night .person .role { font-size: 11px; font-weight: 300; }
  .night .phone { position: absolute; right: 23px; top: 172px; font-size: 13px; font-weight: 300; }
  .sep { display: inline-block; width: 1px; height: 14px; background: currentColor; margin: 0 3px; }
</style>
</head>
<body>

<section class="card inside" aria-label="Inside spread">
  <div class="info">
    <div class="info-row"><span class="text">Aplly onine:http:/bit.ly/norlandes<br>1300 OUR NORLAND<br><strong>ACN</strong>:482 915 306</span></div>
    <div class="info-row"><span class="text"><strong>Postal addresse</strong>: PO box 2184,Seabrook Q4511</span></div>
    <div class="info-row"><span class="text"><strong>Office location</strong>: Level 2/41<br>Harbour Parade,Seabrook Q 4511</span></div>
  </div>
  <div class="brand-name">Norland Estates</div>
  <svg class="pencil" width="20" height="16" viewBox="0 0 22 18" aria-hidden="true">
    <path d="M2 14 L15 3 L19 7 L6 17 L1 17 Z" fill="var(--pencil)"/>
    <path d="M15 3 L17 1 L21 5 L19 7 Z" fill="var(--pencil-dark)"/>
  </svg>
  <div class="write-lines">
    <div class="write-line"></div><div class="write-line"></div><div class="write-line"></div>
    <div class="write-line"></div><div class="write-line"></div><div class="write-line"></div>
  </div>
  <div class="rule"></div>
  <div class="web">www.norlandestates.com.au</div>
</section>

<section class="card director" aria-label="Director card">
  <div class="brand-name">Norland</div>
  <div class="tagline">estates</div>
  <div class="person">
    <div class="name">CLARA WHITFIELD</div>
    <div>Managing Director/Principal REA</div>
  </div>
  <div class="contacts">
    <div>
      <svg width="14" height="11" viewBox="0 0 14 11" aria-hidden="true"><path d="M1 4 Q7 -1 13 4 L11 5 L10 3 L4 3 L3 5 Z M3 6 L11 6 L12 10 L2 10 Z" fill="currentColor"/></svg>
      1300555019<span class="sep"></span>0400555128
    </div>
    <div>
      <svg width="14" height="11" viewBox="0 0 14 11" aria-hidden="true"><rect x="1" y="1" width="12" height="9" fill="none" stroke="currentColor"/><path d="M1 1 L7 6 L13 1" fill="none" stroke="currentColor"/></svg>
      clara@norlandestates.com.au
    </div>
  </div>
  <div class="skyline" role="img" aria-label="Faint city building illustration"></div>
</section>

<section class="card night" aria-label="Assistant card">
  <div class="badge">
    <div class="brand-name">Norland</div>
    <div class="tagline">estates</div>
  </div>
  <div class="person">
    <div class="name">Petra Lindqvist</div>
    <div class="role">Rental Manager</div>
  </div>
  <div class="phone">
    <svg width="16" height="12" viewBox="0 0 14 11" aria-hidden="true"><path d="M1 4 Q7 -1 13 4 L11 5 L10 3 L4 3 L3 5 Z M3 6 L11 6 L12 10 L2 10 Z" fill="currentColor"/></svg>
    1300 555019<span class="sep"></span>0400 555376
  </div>
</section>

</body>
</html>
```